The K7 Momentum Collective Website

We have a pitch deck and messaging drafted. Target audience is academic institutions and VC investors that have seed money in start ups.

Need a basic website

Industry/Entity Type

LIfe Science, Diagnostic, medical device.

Coding

Coded - Design and coding required

Number of Pages Required

5+ page

```html
<!DOCTYPE html>
<html lang="en">
<head>
<meta charset="utf-8">
<title>The K7 Momentum Collective</title>
<link href="https://fonts.googleapis.com/css2?family=Montserrat:wght@400;500;600;700;800&display=swap" rel="stylesheet">
<style>
:root{
  --blue:#0a6cc0;
  --blue-dark:#0758a0;
  --navy:#0a1826;
  --ink:#1a1a1a;
  --muted:#3a3a3a;
  --grey:#dedede;
  --card:#e6e6e6;
  --line:#8a8a8a;
  --white:#ffffff;
}
*{box-sizing:border-box;margin:0;padding:0}
html,body{width:1200px;height:4373px;overflow:hidden;background:var(--white)}
body{font-family:'Montserrat',sans-serif;color:var(--ink);position:relative}
section,header,footer{position:absolute;left:0;width:1200px}
.abs{position:absolute}
.btn{display:inline-block;border-radius:20px;font-size:12px;font-weight:600;padding:9px 16px;letter-spacing:.2px;white-space:nowrap}
.btn-solid{background:var(--blue);color:var(--white)}
.btn-ghost{border:1.5px solid currentColor}

/* header */
.site-header{top:0;height:73px;background:var(--white)}
.brand{left:48px;top:22px;display:flex;align-items:center;gap:8px;color:var(--blue);font-size:10px;font-weight:700;width:130px;line-height:1.2}
.brand-dot{width:22px;height:22px;border-radius:50%;background:var(--blue);flex:none}
.main-nav{left:428px;top:29px;display:flex;gap:27px;font-size:11.5px;font-weight:600;white-space:nowrap}
.main-nav .current{color:var(--blue)}
.sign-in{left:1024px;top:21px;padding:8px 18px}
.search{left:1126px;top:26px}

/* hero */
.hero{top:73px;height:577px;background:linear-gradient(160deg,#6f8aa5 0%,#3b5a7a 35%,#1c3652 65%,#0f2036 100%)}
.hero h1{left:114px;top:125px;font-size:46px;font-weight:800;color:var(--white);line-height:52px}
.hero p{left:114px;top:246px;font-size:13px;color:var(--white);width:240px;line-height:19px}
.hero .btn{left:114px;top:302px;font-size:11px}

/* about */
.about{top:679px;height:375px}
.about-photo{left:0;top:0;width:590px;height:375px;background:linear-gradient(180deg,#3c6f7a 0%,#1b3a46 55%,#0b1a22 100%)}
.about h2{left:622px;top:56px;font-size:34px;font-weight:800}
.about p{left:622px;top:108px;width:460px;font-size:11.5px;line-height:19px;color:var(--muted)}
.about .btn{left:622px;top:284px;font-size:11px}

/* guide band */
.guide{top:1086px;height:377px;background:linear-gradient(90deg,var(--navy) 0%,#0c2238 55%,#0d3150 100%)}
.guide h2{left:122px;top:95px;font-size:34px;font-weight:700;color:var(--white);line-height:44px;white-space:nowrap}
.guide p{left:122px;top:196px;font-size:12px;color:var(--white)}
.guide .btns{left:122px;top:249px;display:flex;gap:12px}
.guide .btn{font-size:11px;color:var(--white)}

/* newsletter */
.daily{top:1497px;height:254px}
.daily-photo{left:0;top:0;width:590px;height:254px;background:linear-gradient(120deg,#c9a57b 0%,#d9d3c9 45%,#e9e9e9 100%)}
.daily h2{left:622px;top:42px;font-size:33px;font-weight:700}
.daily p{left:622px;top:100px;font-size:12px;color:var(--muted)}
.daily .field{left:622px;top:148px;width:346px;height:44px;border:1.5px solid #9a9a9a;background:#f2f2f2;font-size:12px;color:#8a8a8a;padding:14px 25px}
.daily .submit{left:975px;top:148px;height:44px;width:92px;background:var(--blue);color:var(--white);font-size:12px;font-weight:600;display:flex;align-items:center;justify-content:center}

/* services */
.services{top:1789px;height:339px;background:var(--grey)}
.services h2{left:0;width:1200px;top:34px;text-align:center;font-size:33px;font-weight:800}
.service-list{left:51px;top:98px;display:flex;gap:17px}
.service{width:207px;height:204px;border:1.5px solid var(--line);background:var(--card);padding:14px 14px}
.service svg{display:block;margin-bottom:10px}
.service h3{font-size:9.5px;font-weight:700;margin-bottom:6px;white-space:nowrap;letter-spacing:-.2px}
.service p{font-size:9px;line-height:13px;color:var(--muted)}

/* blogs */
.blogs-title{top:2158px;height:50px;text-align:center;font-size:33px;font-weight:700}
.blog-grid{top:2235px;height:687px}
.ph{position:absolute}
.blog-text{position:absolute;padding:0 24px}
.blog-text time{display:block;font-size:9.5px;margin-bottom:7px}
.blog-text h3{font-size:14px;font-weight:700;line-height:18px}
.blog-blue{background:var(--blue);color:var(--white)}
.lab-caption{left:0;top:300px;width:599px;height:73px;background:rgba(225,232,238,.9);padding:14px 40px 0 48px}

/* partners */
.partners{top:2953px;height:551px;background:var(--grey)}
.partners h2{left:0;width:1200px;top:24px;text-align:center;font-size:33px;font-weight:700}
.partner{top:81px;width:360px;text-align:center}
.portrait{width:197px;height:197px;border-radius:50%;margin:0 auto;background:radial-gradient(circle at 50% 40%,#c9b3a3 0%,#8c7a70 60%,#5d6066 100%)}
.partner h3{margin-top:38px;font-size:22px;font-weight:600}
.partner p{margin:12px auto 0;width:285px;font-size:11.5px;line-height:19px;color:var(--muted)}
.contact-icons{margin-top:18px;display:flex;justify-content:center;gap:18px}
.icon-chip{width:20px;height:20px;border-radius:50%;background:#cfe0f0;display:flex;align-items:center;justify-content:center}

/* join */
.join{top:3504px;height:447px}
.join h2{left:122px;top:94px;font-size:24px;font-weight:700;line-height:38px;white-space:nowrap}
.join p{left:122px;top:228px;font-size:17px;font-weight:500}
.join .btns{left:122px;top:305px;display:flex;gap:8px}
.join-photo{left:609px;top:34px;width:591px;height:377px;background:linear-gradient(180deg,#55687e 0%,#8d97a6 45%,#c9a27a 70%,#2c2c2f 100%)}

/* help */
.help{top:3951px;height:166px;background:var(--blue);text-align:center;color:var(--white)}
.help h2{margin-top:32px;font-size:33px;font-weight:700}
.help .btns{margin-top:14px;display:flex;justify-content:center;gap:12px}
.help .btn{font-size:11px;padding:7px 14px}
.help .btn-light{background:var(--white);color:var(--ink)}

/* footer */
.site-footer{top:4117px;height:256px}
.site-footer h4{left:48px;top:98px;font-size:18px;font-weight:700}
.site-footer .lede{left:48px;top:126px;font-size:12px}
.foot-field{left:48px;top:155px;width:253px;height:34px;border:1.5px solid #9a9a9a;border-radius:18px;font-size:12px;color:#8a8a8a;padding:9px 18px}
.foot-submit{left:313px;top:155px;width:103px;height:34px;border-radius:18px;background:var(--blue);color:var(--white);font-size:12px;font-weight:600;display:flex;align-items:center;justify-content:center}
.foot-nav{left:577px;top:142px;display:flex;gap:25px;font-size:11.5px;font-weight:500;white-space:nowrap}
.foot-legal{left:850px;top:170px;display:flex;gap:40px;font-size:9px;white-space:nowrap}
.foot-rule{left:48px;top:204px;width:1102px;height:1px;background:#555}
.copyright{left:48px;top:222px;font-size:11px}
.socials{left:964px;top:214px;display:flex;gap:26px}
.social{width:26px;height:26px;border-radius:50%;background:#000}
</style>
</head>
<body>

<header class="site-header">
  <div class="abs brand"><span class="brand-dot"></span><span>The K7 Momentum Collective</span></div>
  <nav class="abs main-nav">
    <span class="current">HOME</span><span>ABOUT US</span><span>SERVICES</span><span>BLOGS</span><span>PARTNERS</span><span>CAREERS</span><span>CONTACT</span>
  </nav>
  <span class="abs btn btn-solid sign-in">SIGN IN</span>
  <svg class="abs search" width="18" height="18" viewBox="0 0 18 18"><circle cx="7.5" cy="7.5" r="5.5" fill="none" stroke="#1a1a1a" stroke-width="1.8"/><line x1="11.5" y1="11.5" x2="16" y2="16" stroke="#1a1a1a" stroke-width="1.8"/></svg>
</header>

<section class="hero" role="img" aria-label="Businessman touching a rising white arrow among upward arrows">
  <h1 class="abs">MADE FOR<br>CHANGE</h1>
  <p class="abs">It's time to set the foundation for a made-for-change future.</p>
  <span class="abs btn btn-solid">LEARN MORE</span>
</section>

<section class="about">
  <div class="abs about-photo" role="img" aria-label="Silhouettes of business people standing in front of a city window"></div>
  <h2 class="abs">ABOUT US</h2>
  <p class="abs">The K7 Momentum Collective (K7) is a group of experienced executives whose careers have been focused on taking innovative ideas to market by strategically navigating the buildout of best-in-class life science and diagnostic organizations. This experience makes us uniquely equipped to be involved in all aspects of our due diligence on new or existing investments (business analysis, industry thesis, competitive landscape, business/pricing model, and financial modeling as it relates to validation of the assumptions in the model to determine the return expectations).</p>
  <span class="abs btn btn-solid">KNOW MORE</span>
</section>

<section class="guide">
  <svg class="abs" style="left:620px;top:70px" width="520" height="250" viewBox="0 0 520 250" role="img" aria-label="Hand touching a glowing line chart above a tablet">
    <polyline points="40,200 110,170 170,190 230,120 300,20 340,150 390,90 430,160 500,140" fill="none" stroke="#5fc4ff" stroke-width="3"/>
    <ellipse cx="260" cy="215" rx="230" ry="22" fill="#1b4e7a" opacity=".6"/>
  </svg>
  <h2 class="abs">The executive's guide to<br>new-business building</h2>
  <p class="abs">How to master the most important growth game.</p>
  <div class="abs btns"><span class="btn btn-solid">STAY FOCUSED</span><span class="btn btn-ghost">EXPLORE MORE</span></div>
</section>

<section class="daily">
  <div class="abs daily-photo" role="img" aria-label="Hands holding a phone showing a newsletter signup over a keyboard"></div>
  <h2 class="abs">Get your Daily Read</h2>
  <p class="abs">Our must-read reports of the day, delivered to your inbox daily.</p>
  <div class="abs field">Email Address</div>
  <div class="abs submit">SUBSCRIBE</div>
</section>

<section class="services">
  <h2 class="abs">OUR SERVICES</h2>
  <div class="abs service-list">
    <article class="service">
      <svg width="40" height="40" viewBox="0 0 40 40"><rect x="4" y="6" width="24" height="28" fill="none" stroke="#0a6cc0" stroke-width="2"/><line x1="9" y1="14" x2="23" y2="14" stroke="#0a6cc0" stroke-width="2"/><line x1="9" y1="20" x2="23" y2="20" stroke="#0a6cc0" stroke-width="2"/><circle cx="30" cy="28" r="6" fill="none" stroke="#0a6cc0" stroke-width="2"/></svg>
      <h3>Reviewing Business Plans</h3>
      <p>Reading/reviewing business plans and pitch decks, which may include the inventor disclosure(s), provisional patent(s), and inventor interview.</p>
    </article>
    <article class="service">
      <svg width="40" height="40" viewBox="0 0 40 40"><path d="M20 4 L32 36 H8 Z" fill="none" stroke="#0a6cc0" stroke-width="2"/><circle cx="8" cy="10" r="3" fill="#0a6cc0"/><circle cx="15" cy="10" r="3" fill="#0a6cc0"/></svg>
      <h3>Assessing Market Attractiveness</h3>
      <p>Assessing market/company attractiveness through identification of product definition and target market segments, as well as a competitor analysis to help identify potential revenue growth and traction.</p>
    </article>
    <article class="service">
      <svg width="40" height="40" viewBox="0 0 40 40"><circle cx="12" cy="12" r="5" fill="none" stroke="#0a6cc0" stroke-width="2"/><circle cx="28" cy="12" r="5" fill="none" stroke="#0a6cc0" stroke-width="2"/><path d="M4 34 Q12 20 20 34 Q28 20 36 34" fill="none" stroke="#0a6cc0" stroke-width="2"/></svg>
      <h3>Strategic Mentor</h3>
      <p>Working in a strategic capacity with existing portfolio companies as either a coach/mentor role or as a fractional executive team member as needed.</p>
    </article>
    <article class="service">
      <svg width="40" height="40" viewBox="0 0 40 40"><rect x="4" y="4" width="18" height="22" fill="none" stroke="#0a6cc0" stroke-width="2"/><rect x="14" y="24" width="4" height="10" fill="#0a6cc0"/><rect x="21" y="18" width="4" height="16" fill="#0a6cc0"/><rect x="28" y="12" width="4" height="22" fill="#0a6cc0"/></svg>
      <h3>Market Analyses Report</h3>
      <p>Preparing market analyses and presentations to assist with investment decisions and for engagement with the firm's extensive network of corporate relationships.</p>
    </article>
    <article class="service">
      <svg width="40" height="40" viewBox="0 0 40 40"><rect x="4" y="4" width="32" height="8" fill="#0a6cc0"/><circle cx="13" cy="20" r="4" fill="none" stroke="#0a6cc0" stroke-width="2"/><circle cx="27" cy="20" r="4" fill="none" stroke="#0a6cc0" stroke-width="2"/><rect x="4" y="28" width="32" height="6" fill="none" stroke="#0a6cc0" stroke-width="2"/></svg>
      <h3>Internal Meetings</h3>
      <p>The K7 partners will be made available to participate in and if asked to contribute to weekly internal meetings in which new investments and portfolio companies are discussed.</p>
    </article>
  </div>
</section>

<h2 class="blogs-title abs" style="left:0;width:1200px">Blogs</h2>

<section class="blog-grid">
  <div class="ph" style="left:0;top:0;width:599px;height:373px;background:linear-gradient(135deg,#cfdbe4 0%,#8fb4cf 45%,#4d7ea4 100%)" role="img" aria-label="Lab worker in protective clothing operating manufacturing equipment"></div>
  <div class="blog-text lab-caption abs"><time>January 17, 2023</time><h3>The K7 Momentum Collective joins corporate affiliate program at Halden Institute for AI to bring AI and frontier tech to clients.</h3></div>

  <div class="ph" style="left:599px;top:0;width:302px;height:229px;background:linear-gradient(180deg,#7ea05a 0%,#4d7a3a 60%,#6a5a48 100%)" role="img" aria-label="Group of young people cheering outdoors among trees"></div>
  <div class="blog-text" style="left:892px;top:147px;width:308px"><time>January 29, 2023</time><h3>New look at human development points way to inclusive growth</h3></div>

  <div class="blog-text blog-blue" style="left:599px;top:229px;width:601px;height:144px;padding-top:46px"><time>February 9, 2023</time><h3>The K7 Momentum Collective announces six members of 2023 External Advisory Group</h3></div>

  <div class="blog-text" style="left:24px;top:541px;width:250px;padding:0"><time>February 17, 2023</time><h3>New tech accelerator propels underrepresented founders to success</h3></div>
  <div class="ph" style="left:283px;top:373px;width:316px;height:314px;background:linear-gradient(180deg,#aab8c6 0%,#8a96a4 50%,#55606c 100%)" role="img" aria-label="Business people shaking hands on a balcony above a city"></div>

  <div class="blog-text" style="left:599px;top:541px;width:285px"><time>February 21, 2023</time><h3>The K7 Momentum Collective co-founds effort to transform agriculture and food systems in Africa</h3></div>
  <div class="ph" style="left:884px;top:373px;width:316px;height:314px;background:linear-gradient(160deg,#6b8a3e 0%,#8a6a3e 55%,#5a3c26 100%)" role="img" aria-label="Farmers working the soil in a field"></div>
</section>

<section class="partners">
  <h2 class="abs">Our Partners</h2>
  <article class="abs partner" style="left:97px">
    <div class="portrait" role="img" aria-label="Portrait photo of RM Dalton"></div>
    <h3>RM Dalton</h3>
    <p>RM is a proven marketing, sales and operations executive leader in the life science and diagnostic industries. She has extensive experience in assessing and developing business plans and growth strategies that include business analysis, industry thesis,</p>
    <div class="contact-icons">
      <span class="icon-chip"><svg width="10" height="10" viewBox="0 0 10 10"><path d="M2 1 L4 3 L3 4 Q4 6 6 7 L7 6 L9 8 L8 9 Q3 9 1 2 Z" fill="#0a6cc0"/></svg></span>
      <span class="icon-chip"><svg width="12" height="9" viewBox="0 0 12 9"><rect x=".5" y=".5" width="11" height="8" fill="#0a6cc0"/><polyline points=".5,.5 6,5 11.5,.5" fill="none" stroke="#fff"/></svg></span>
      <span class="icon-chip"><svg width="8" height="8"><rect width="8" height="8" fill="#0a6cc0"/></svg></span>
    </div>
  </article>
  <article class="abs partner" style="left:419px">
    <div class="portrait" role="img" aria-label="Portrait photo of KL Ferris"></div>
    <h3>KL Ferris</h3>
    <p>KL is an accomplished CEO and well-rounded executive with more than 25 years of experience in medical devices, research tools and diagnostics. He has extensive experience in strategy development &amp; deployment, corporate development, private &amp; public</p>
    <div class="contact-icons">
      <span class="icon-chip"><svg width="10" height="10" viewBox="0 0 10 10"><path d="M2 1 L4 3 L3 4 Q4 6 6 7 L7 6 L9 8 L8 9 Q3 9 1 2 Z" fill="#0a6cc0"/></svg></span>
      <span class="icon-chip"><svg width="12" height="9" viewBox="0 0 12 9"><rect x=".5" y=".5" width="11" height="8" fill="#0a6cc0"/><polyline points=".5,.5 6,5 11.5,.5" fill="none" stroke="#fff"/></svg></span>
      <span class="icon-chip"><svg width="8" height="8"><rect width="8" height="8" fill="#0a6cc0"/></svg></span>
    </div>
  </article>
  <article class="abs partner" style="left:743px">
    <div class="portrait" role="img" aria-label="Portrait photo of Nora Whitlock"></div>
    <h3>Nora Whitlock</h3>
    <p>Nora has over 30 years of experience in the quality, regulatory and operations field in medical devices, companion diagnostics, education, and health care systems. She has extensive executive experience in establishing the quality and regulatory path</p>
    <div class="contact-icons">
      <span class="icon-chip"><svg width="10" height="10" viewBox="0 0 10 10"><path d="M2 1 L4 3 L3 4 Q4 6 6 7 L7 6 L9 8 L8 9 Q3 9 1 2 Z" fill="#0a6cc0"/></svg></span>
      <span class="icon-chip"><svg width="12" height="9" viewBox="0 0 12 9"><rect x=".5" y=".5" width="11" height="8" fill="#0a6cc0"/><polyline points=".5,.5 6,5 11.5,.5" fill="none" stroke="#fff"/></svg></span>
      <span class="icon-chip"><svg width="8" height="8"><rect width="8" height="8" fill="#0a6cc0"/></svg></span>
    </div>
  </article>
</section>

<section class="join">
  <h2 class="abs">WHAT WOULD YOU DO IF YOU<br>HAD THE CHANCE TO BUILD THE<br>WORLD YOU WANT TO LIVE IN?</h2>
  <p class="abs">Join The K7 Momentum Collective</p>
  <div class="abs btns"><span class="btn btn-solid" style="padding:8px 26px">CAREERS</span><span class="btn btn-ghost" style="padding:7px 12px">SEARCH &amp; APPLY</span></div>
  <div class="abs join-photo" role="img" aria-label="Silhouettes of people raising their arms at sunset above a city"></div>
</section>

<section class="help">
  <h2>How can we help you?</h2>
  <div class="btns"><span class="btn btn-light">GET IN TOUCH</span><span class="btn btn-ghost">FIND MORE</span></div>
</section>

<footer class="site-footer">
  <h4 class="abs">Subscribe</h4>
  <p class="abs lede">Select topics and stay connect with our latest Topics</p>
  <div class="abs foot-field">Email Address</div>
  <div class="abs foot-submit">SUBMIT</div>
  <nav class="abs foot-nav"><span>HOME</span><span>ABOUT US</span><span>SERVICES</span><span>BLOGS</span><span>PARTNERS</span><span>CAREERS</span><span>CONTACT</span></nav>
  <div class="abs foot-legal"><span>Local language information</span><span>Accessibility statement</span></div>
  <div class="abs foot-rule"></div>
  <p class="abs copyright">©The K7 Momentum Collective 56. AllRight Reserved.</p>
  <div class="abs socials"><span class="social"></span><span class="social"></span><span class="social"></span><span class="social"></span></div>
</footer>

</body>
</html>
```